We would like a business card that includes our logo on the front and the following information on the back:

Warren Pike, Owner
Phone: (555) 614-0827
email: wpikefencing@brookmail.example

Wally Pike & Sons Fencing provides the following services:
Barbed wire
Smooth wire
High tensile
Electric

On the bottom of the card please add:
Please call or email Warren for estimates.

```html
<!DOCTYPE html>
<html lang="en">
<head>
<meta charset="utf-8">
<title>Wally Pike &amp; Sons Fencing – Business Card</title>
<link rel="stylesheet" href="https://fonts.googleapis.com/css2?family=EB+Garamond:wght@400;500;700&display=swap">
<style>
  :root {
    --backdrop: #d9d9d9;
    --card-white: #ffffff;
    --saddle-brown: #7d5136;
    --wire-tone: #a27a60;
    --ink: #1e1a18;
    --cream: #f7f1ea;
  }
  * { box-sizing: border-box; margin: 0; padding: 0; }
  html, body {
    width: 1200px;
    height: 846px;
    overflow: hidden;
    background: var(--backdrop);
    font-family: "EB Garamond", Garamond, serif;
  }
  .sheet {
    width: 1200px;
    height: 846px;
    display: flex;
    align-items: center;
    justify-content: center;
    gap: 40px;
  }
  .card {
    width: 540px;
    height: 309px;
    position: relative;
    box-shadow: 0 6px 18px rgba(0,0,0,0.18);
  }

  /* Front */
  .card-front {
    background: var(--card-white);
    display: flex;
    flex-direction: column;
    align-items: center;
    justify-content: center;
    gap: 18px;
  }
  .brand-mark {
    width: 44px;
    height: 44px;
    background: var(--saddle-brown);
  }
  .brand-name {
    font-size: 34px;
    font-weight: 500;
    color: var(--ink);
    letter-spacing: 0.5px;
    text-transform: uppercase;
  }

  /* Back */
  .card-back {
    background: var(--saddle-brown);
    color: var(--cream);
    text-align: center;
    overflow: hidden;
  }
  .contact {
    position: absolute;
    top: 34px;
    left: 0;
    right: 0;
  }
  .contact-name {
    font-size: 21px;
    font-weight: 700;
    margin-bottom: 6px;
  }
  .contact-line {
    font-size: 15px;
    line-height: 1.45;
    display: flex;
    align-items: center;
    justify-content: center;
    gap: 6px;
  }
  .contact-line svg { width: 12px; height: 12px; fill: var(--cream); }
  .wire-band {
    position: absolute;
    left: 0;
    right: 0;
    top: 142px;
    height: 34px;
    background: linear-gradient(90deg, var(--saddle-brown), var(--wire-tone) 50%, var(--saddle-brown));
  }
  .services {
    position: absolute;
    left: 0;
    right: 0;
    bottom: 26px;
    font-size: 12.5px;
    letter-spacing: 0.4px;
    text-transform: uppercase;
    line-height: 1.55;
  }
  .services .call-to-action {
    font-weight: 700;
    margin-top: 6px;
  }
</style>
</head>
<body>
<main class="sheet">
  <section class="card card-front">
    <div class="brand-mark"></div>
    <h1 class="brand-name">Wally Pike &amp; Sons Fencing</h1>
  </section>

  <section class="card card-back">
    <div class="contact">
      <p class="contact-name">Warren Pike, owner</p>
      <p class="contact-line">
        <svg viewBox="0 0 24 24" aria-hidden="true"><path d="M6.6 10.8a15.5 15.5 0 0 0 6.6 6.6l2.2-2.2a1 1 0 0 1 1-.25 11.4 11.4 0 0 0 3.6.57 1 1 0 0 1 1 1V20a1 1 0 0 1-1 1A17 17 0 0 1 3 4a1 1 0 0 1 1-1h3.5a1 1 0 0 1 1 1c0 1.25.2 2.46.57 3.6a1 1 0 0 1-.25 1z"/></svg>
        (555) 614-0827
      </p>
      <p class="contact-line">
        <svg viewBox="0 0 24 24" aria-hidden="true"><path d="M2 5h20v14H2z M2 5l10 8 10-8" fill="none" stroke="#f7f1ea" stroke-width="2"/></svg>
        wpikefencing@brookmail.example
      </p>
    </div>

    <div class="wire-band" role="img" aria-label="Illustration of a strand of barbed wire crossing the card"></div>

    <div class="services">
      <p>Wally Pike &amp; Sons Fencing provides the following services:</p>
      <p>Barbed wire • Smooth wire • High tensile • Electric</p>
      <p class="call-to-action">Please call or email Warren for estimates</p>
    </div>
  </section>
</main>
</body>
</html>
```